Tidewell HVAC WordPress website design

Design a new modern, clean, website for HVAC mechanical business that uses company logo/colors for branding and recognition. Files attached are just for band and color information. Here is a website design that appeals to me https://www.quillerbyhomes.example/

A clear description of who we are and what we do

An easily-navigated site map

An easily-navigated site map for mobile devices

Easy-to-find contact information

Obvious call to action for service, installs or to schedule estimates

about us page

Provide a way for potential customers to contact us via text or email

provide a way that allows a customer to upload a picture to request a service call or quote.
Updates

I'm looking for the design to be completed in WordPress

Industry/Entity Type

HVAC Mechanical & Building Automation / Controls contractor

Coding

Coded - Design and coding required

Number of Pages Required

5+ page

Colors
0054AA
0677BA
7BADD7
CADEEF
E8F1F8

Requirements
Must have
• Design a new modern, clean, website for HVAC mechanical business that uses company logo/colors for branding and recognition. Files attached are just for band and color information. Here is a website design that appeals to me https://www.quillerbyhomes.example/ A clear description of who we are and what we do An easily-navigated site map An easily-navigated site map for mobile devices Easy-to-find contact information Obvious call to action for service, installs or to schedule estimates about us page Provide a way for potential customers to contact us via text or email provide a way that allows a customer to upload a picture to request a service call or quote.
Nice to have

```html
<!DOCTYPE html>
<html lang="en">
<head>
<meta charset="utf-8">
<title>Tidewell HVAC</title>
<link href="https://fonts.googleapis.com/css2?family=Inter:wght@400;500;600;700;800&display=swap" rel="stylesheet">
<style>
:root{
  --page-bg:#e4f0fb;
  --header-bg:#232323;
  --brand-blue:#0a7fe6;
  --brand-blue-dark:#0054aa;
  --text-light:#ffffff;
  --text-muted:#d8d8d8;
  --text-dark:#111111;
  --field-bg:#ffffff;
  --placeholder:#8a8a8a;
  --card-bg:rgba(236,236,240,0.86);
}
*{box-sizing:border-box;margin:0;padding:0}
html,body{width:1200px;height:900px;overflow:hidden}
body{background:linear-gradient(180deg,#dfeefb 0%,#eef6fd 100%);font-family:'Inter',sans-serif;position:relative}
.site{position:absolute;left:60px;top:48px;width:1080px;height:900px;border-radius:14px 14px 0 0;overflow:hidden;background:var(--header-bg)}
.site-header{height:85px;display:flex;align-items:center;position:relative}
.brand{position:absolute;left:165px;top:21px;display:flex;align-items:center;gap:10px;color:var(--text-light);font-weight:700;font-size:21px}
.brand-mark{width:40px;height:40px;border-radius:50%;background:var(--brand-blue)}
.main-nav{position:absolute;left:466px;top:32px;display:flex;gap:0}
.main-nav a{color:var(--text-muted);text-decoration:none;font-size:16px;font-weight:500;position:absolute;white-space:nowrap}
.main-nav a.current{color:var(--text-light)}
.call-button{position:absolute;left:802px;top:24px;width:171px;height:38px;background:var(--brand-blue);border-radius:3px;display:flex;align-items:center;justify-content:center;gap:8px;color:var(--text-light);font-weight:600;font-size:16px}
.hero{position:absolute;left:0;top:85px;width:1080px;height:564px;overflow:hidden}
.hero-photo{position:absolute;inset:0;background:
  linear-gradient(180deg,rgba(120,70,170,0) 0%,rgba(0,0,0,0) 55%),
  linear-gradient(180deg,#5a3f9a 0%,#8a5fb4 18%,#6a4f92 32%,#7a5a48 52%,#a27a3a 66%,#4c4a70 84%,#4b5fb8 100%)}
.hero-photo::after{content:"";position:absolute;inset:0;background:linear-gradient(90deg,rgba(0,0,0,0.25) 0%,rgba(0,0,0,0.05) 60%,rgba(0,0,0,0.1) 100%)}
.hero-copy{position:absolute;left:165px;top:121px;color:var(--text-light)}
.hero-kicker{font-size:12px;font-weight:500}
.hero-title{margin-top:14px;font-size:60px;font-weight:800;line-height:73px;letter-spacing:-0.5px}
.badges{position:absolute;left:169px;top:457px;display:flex;gap:13px}
.badge{width:45px;height:50px;background:#f4f4f4;border-radius:5px;display:flex;align-items:center;justify-content:center}
.badge span{width:28px;height:28px;border-radius:50%;background:#2b5aa8}
.badge:nth-child(1) span{background:#c8342c}
.badge:nth-child(3) span{background:#3a2f8a}
.hero-rule{position:absolute;left:165px;top:517px;width:401px;height:1px;background:rgba(255,255,255,0.7)}
.quote-form{position:absolute;left:697px;top:164px;width:302px;height:355px;background:var(--card-bg);border-radius:9px;padding:20px 38px 0 37px}
.quote-form h2{text-align:center;font-size:14px;font-weight:600;color:var(--text-dark);margin-bottom:21px}
.field label{display:block;font-size:9.5px;font-weight:500;color:var(--text-dark);margin-bottom:3px}
.field .input{height:37px;background:var(--field-bg);display:flex;align-items:center;justify-content:space-between;padding:0 10px;font-size:7.5px;color:var(--placeholder);margin-bottom:13px}
.quote-button{margin-top:3px;margin-left:-6px;width:233px;height:38px;background:var(--brand-blue);border-radius:2px;color:var(--text-light);font-weight:700;font-size:15px;display:flex;align-items:center;justify-content:center}
.services{position:absolute;left:0;top:649px;width:1080px;height:300px;background:linear-gradient(180deg,#222 0%,#0f0f0f 100%)}
.services h2{text-align:center;color:var(--text-light);font-size:37px;font-weight:700;margin-top:41px}
.service-card{position:absolute;top:138px;width:207px;height:120px;background:#f7f7f7;border-radius:8px}
.service-card svg{position:absolute;left:50%;top:36px;transform:translateX(-50%)}
</style>
</head>
<body>
<div class="site">
  <header class="site-header">
    <div class="brand"><span class="brand-mark"></span>Tidewell HVAC</div>
    <nav class="main-nav">
      <a class="current" style="left:0">Home</a>
      <a style="left:69px">Services</a>
      <a style="left:159px">Contact</a>
      <a style="left:244px">About</a>
    </nav>
    <div class="call-button">
      <svg width="22" height="22" viewBox="0 0 24 24" fill="none" stroke="#fff" stroke-width="1.6"><circle cx="12" cy="12" r="11"/><path d="M8.5 6.5l2 2.2-1.2 1.6c.7 1.6 2 2.9 3.5 3.6l1.6-1.2 2.2 2-1.2 1.8c-3.8-.3-7.5-4-7.9-7.9z" fill="#fff" stroke="none"/></svg>
      555-014-2290
    </div>
  </header>

  <section class="hero">
    <div class="hero-photo" role="img" aria-label="Night city skyline with lit towers reflected in a river"></div>
    <div class="hero-copy">
      <p class="hero-kicker">HVAC Mechanical &amp; Building Automation / Controls contractor</p>
      <h1 class="hero-title">Your Trusted<br>HVAC Solutions<br>Provider</h1>
    </div>
    <div class="badges">
      <div class="badge"><span></span></div>
      <div class="badge"><span></span></div>
      <div class="badge"><span></span></div>
    </div>
    <div class="hero-rule"></div>

    <form class="quote-form">
      <h2>Schedule your service</h2>
      <div class="field"><label>Name</label><div class="input">e.g Jhon Doe</div></div>
      <div class="field"><label>Phone</label><div class="input">e.g 1 - 555 5555 5555</div></div>
      <div class="field"><label>Service</label><div class="input">Select Service
        <svg width="16" height="9" viewBox="0 0 16 9" fill="none" stroke="#555" stroke-width="1.3"><path d="M1 1l7 7 7-7"/></svg></div></div>
      <div class="field"><label>Time</label><div class="input">Schedule Time
        <svg width="16" height="9" viewBox="0 0 16 9" fill="none" stroke="#555" stroke-width="1.3"><path d="M1 1l7 7 7-7"/></svg></div></div>
      <div class="quote-button">Request a quote</div>
    </form>
  </section>

  <section class="services">
    <h2>Our Services</h2>
    <div class="service-card" style="left:184px">
      <svg width="80" height="40" viewBox="0 0 80 40"><circle cx="40" cy="22" r="8" fill="#1a73d9"/><ellipse cx="40" cy="8" rx="10" ry="8" fill="#1a73d9"/><ellipse cx="20" cy="30" rx="12" ry="7" fill="#1a73d9"/><ellipse cx="60" cy="30" rx="12" ry="7" fill="#1a73d9"/></svg>
    </div>
    <div class="service-card" style="left:436px">
      <svg width="60" height="40" viewBox="0 0 60 40"><path d="M30 6L8 34h44z" fill="#1a73d9"/></svg>
    </div>
    <div class="service-card" style="left:688px">
      <svg width="70" height="40" viewBox="0 0 70 40"><rect x="22" y="0" width="4" height="14" fill="#ddd"/><rect x="44" y="0" width="4" height="14" fill="#ddd"/><rect x="10" y="12" width="50" height="28" rx="3" fill="#ececec"/><rect x="14" y="16" width="42" height="24" fill="#1a73d9"/><rect x="28" y="22" width="14" height="3" fill="#fff"/></svg>
    </div>
  </section>
</div>
</body>
</html>
```